Business Card for staff member of football club SC Brenval

I would like to get a business card template for all staff member of our soccer club.

The card should use as much as possible the 2 colors of the club : Red which is the main color and blue which is the alternative color. It can be balanced between the two like our logo.

I prefer simple and lean design.

Contact Information for Business Card

Bussiness card should have all main stuff as describe here below in must have.

Font styles to use
Sans Serif

Requirements
Must have
• Name : Laurent DESPRATIN
Fonction : Président
Mobile : +41 xx xxx xx xx
Email : first.lastname@scbrenval.ch
Adresse of the club : SC Brenval, 1873 Brenval
Website of the club : www.scbrenval.ch
Nice to have
• Version with and without picture of the staff member

A version for men, a version for women staff member.

```html
<!DOCTYPE html>
<html lang="en">
<head>
<meta charset="utf-8">
<title>SC Brenval – Staff Business Card</title>
<link rel="stylesheet" href="https://fonts.googleapis.com/css2?family=Mulish:ital,wght@0,400;0,700;0,800;1,400&display=swap">
<style>
  :root {
    --club-red: #e8243a;
    --club-blue: #0f87c8;
    --card-white: #ffffff;
    --card-edge: #8a8a8a;
    --ink: #1e1e1e;
    --photo-tone: #a88a6c;
    --page: #ffffff;
  }
  html, body {
    margin: 0;
    padding: 0;
    width: 1200px;
    height: 900px;
    overflow: hidden;
    background: var(--page);
  }
  .sheet {
    position: relative;
    width: 1200px;
    height: 900px;
    font-family: "Mulish", sans-serif;
  }
  .card {
    position: absolute;
    width: 256px;
    height: 370px;
    overflow: visible;
  }
  .card--front-photo { left: 85px;  top: 40px; }
  .card--back-top    { left: 446px; top: 40px; }
  .card--front-plain { left: 85px;  top: 490px; }
  .card--back-bottom { left: 446px; top: 490px; }

  .pennant { fill: var(--card-white); stroke: var(--card-edge); stroke-width: 1; }
  .band-red { fill: var(--club-red); }
  .band-blue { fill: var(--club-blue); }
  .photo-ring { fill: var(--card-white); }
  .photo { fill: var(--photo-tone); }

  .staff-name { fill: var(--club-red); font-size: 15.5px; letter-spacing: 0.3px; }
  .staff-name .surname { font-weight: 800; }
  .staff-role { fill: var(--club-red); font-size: 12.5px; font-style: italic; }
  .contact { fill: var(--club-blue); font-size: 12.5px; letter-spacing: 0.2px; }
  .club-name { fill: var(--ink); font-size: 34px; font-weight: 800; letter-spacing: -0.5px; }
</style>
</head>
<body>
<main class="sheet">

  <!-- Front with staff photo -->
  <svg class="card card--front-photo" viewBox="0 0 256 370" aria-label="Business card front with photo">
    <path class="pennant" d="M1.5 1.5 H254.5 V282 L127 367 L1.5 282 Z"/>
    <rect class="band-red" x="32" y="1" width="88" height="109"/>
    <rect class="band-blue" x="135" y="1" width="87" height="109"/>
    <circle class="photo-ring" cx="127" cy="67" r="56"/>
    <circle class="photo" cx="127" cy="67" r="50" role="img" aria-label="Portrait photo of the staff member"/>
    <text class="staff-name" x="127" y="141" text-anchor="middle">Laurent <tspan class="surname">DESPRATIN</tspan></text>
    <text class="staff-role" x="127" y="160" text-anchor="middle">President</text>
    <text class="contact" x="127" y="184" text-anchor="middle">+41 xx xxx xx xx</text>
    <text class="contact" x="127" y="204" text-anchor="middle">first.lastname@scbrenval.ch</text>
    <text class="contact" x="127" y="224" text-anchor="middle">SC Brenval, 1873 Brenval</text>
    <text class="contact" x="127" y="244" text-anchor="middle">www.scbrenval.ch</text>
    <polygon class="band-red" points="32,260 120,260 120,322"/>
    <polygon class="band-blue" points="135,260 222,260 135,322"/>
  </svg>

  <!-- Back, club name -->
  <svg class="card card--back-top" viewBox="0 0 256 370" aria-label="Business card back">
    <path class="pennant" d="M1.5 1.5 H254.5 V282 L127 367 L1.5 282 Z"/>
    <text class="club-name" x="127" y="190" text-anchor="middle">SC Brenval</text>
  </svg>

  <!-- Front without photo -->
  <svg class="card card--front-plain" viewBox="0 0 256 370" aria-label="Business card front without photo">
    <path class="pennant" d="M1.5 1.5 H254.5 V282 L127 367 L1.5 282 Z"/>
    <rect class="band-red" x="32" y="1" width="88" height="46"/>
    <rect class="band-blue" x="135" y="1" width="87" height="46"/>
    <text class="staff-name" x="127" y="82" text-anchor="middle">Laurent <tspan class="surname">DESPRATIN</tspan></text>
    <text class="staff-role" x="127" y="104" text-anchor="middle">President</text>
    <text class="contact" x="127" y="133" text-anchor="middle">+41 xx xxx xx xx</text>
    <text class="contact" x="127" y="154" text-anchor="middle">first.lastname@scbrenval.ch</text>
    <text class="contact" x="127" y="176" text-anchor="middle">SC Brenval, 1873 Brenval</text>
    <text class="contact" x="127" y="197" text-anchor="middle">www.scbrenval.ch</text>
    <polygon class="band-red" points="32,215 120,215 120,322 32,262"/>
    <polygon class="band-blue" points="135,215 222,215 222,262 135,322"/>
  </svg>

  <!-- Back, club name -->
  <svg class="card card--back-bottom" viewBox="0 0 256 370" aria-label="Business card back">
    <path class="pennant" d="M1.5 1.5 H254.5 V282 L127 367 L1.5 282 Z"/>
    <text class="club-name" x="127" y="190" text-anchor="middle">SC Brenval</text>
  </svg>

</main>
</body>
</html>
```